Business Card Design

We need a business card design for a Non-Profit Christian Based Organization located in Milford, Pa.
Alder Ridge Helping Harbor
Is a Christ-centered organization dedicated to providing compassion and hope to homeless or near homeless, families and individuals, by meeting their basic and urgent need of food, clothing and shelter.
Updates
the logo is black and white
and must add the color green some where 00400
Industry/Entity Type
Clothing
Contact Information for Business Card
Alder Ridge Helping Harbor
P.O. Box 287
Fernvale, Pa 18429
Phone: (570) 413-CARE(2273)
Toll Free: (855) 413-CARE
email:Info@alderridgehh.org
email:Careline@alderridgehh.org
Our organization already has a logo.
Front of card:
Is a Christ-centered organization dedicated to providing compassion and hope to homeless or near homes, families and individual by meeting their basic and urgent need of food, clothing and shelter.(this is our Mission Statement)
On back of card:
'I was hungry and you gave me something to eat;
"I was thirsty and you gave me something to drink;
"I was a stranger and you invited me in."
Matthew 25:35
Color: Logo is black and white
Background color I would like a bright light green 00ff00(close to that)
I attached a sample of what I created on Quill Press but, I don't like the color green, nor the design (but I just wanted to give you and Idea of the Logo and Alder Ridge (one line) Helping Harbor (second line) in a different font thank you
Delia Rostova
Pr/Board of Directors

```html
<!DOCTYPE html>
<html lang="en">
<head>
<meta charset="utf-8">
<title>Alder Ridge Helping Harbor — Business Card</title>
<link rel="stylesheet" href="https://fonts.googleapis.com/css2?family=Marcellus&family=Parisienne&family=Roboto+Condensed:wght@400&display=swap">
<style>
  :root {
    --card-green: #00a651;
    --title-yellow: #fff200;
    --ink: #333333;
    --mark: #111111;
    --page: #ffffff;
  }
  * { margin: 0; padding: 0; box-sizing: border-box; }
  html, body {
    width: 998px; height: 1200px; overflow: hidden;
    background: var(--page);
  }
  .sheet { position: relative; width: 998px; height: 1200px; }
  .card {
    position: absolute; left: 39px; width: 916px; height: 538px;
    background: var(--card-green);
    font-family: "Roboto Condensed", "Arial Narrow", sans-serif;
    color: var(--ink);
  }
  .card--front { top: 32px; }
  .card--back { top: 625px; }
  .card > * { position: absolute; white-space: nowrap; line-height: 1; }

  .wordmark-title {
    font-family: "Marcellus", serif;
    color: var(--title-yellow);
    text-transform: uppercase;
    letter-spacing: 1px;
    font-weight: 400;
  }
  .wordmark-tagline {
    font-family: "Parisienne", cursive;
    color: var(--ink);
  }
  .mark-spot { background: var(--mark); border-radius: 50%; }

  .front-title { right: 82px; top: 86px; font-size: 58px; }
  .front-tagline { right: 82px; top: 154px; font-size: 42px; }
  .front-mark { left: 100px; top: 196px; width: 150px; height: 150px; }

  .contact { left: 438px; font-size: 24px; }
  .contact dt { display: inline-block; width: 107px; }
  .contact dd { display: inline-block; }
  .address { top: 296px; }
  .phones { top: 351px; line-height: 28px; }
  .emails { top: 437px; line-height: 28px; }
  .emails .line2 { padding-left: 107px; display: block; }
  .front-web { left: 39px; top: 471px; font-size: 24px; }

  .verse {
    right: 82px; top: 22px;
    font-family: "Parisienne", cursive;
    color: var(--title-yellow);
    font-size: 39px; line-height: 54px; text-align: right;
  }
  .verse-ref { right: 82px; top: 200px; font-size: 26px; }
  .back-title { right: 174px; top: 358px; font-size: 46px; }
  .back-tagline { right: 168px; top: 408px; font-size: 32px; }
  .back-mark { left: 750px; top: 318px; width: 90px; height: 90px; }
  .back-web { left: 505px; top: 469px; font-size: 25px; }
</style>
</head>
<body>
<main class="sheet">
  <section class="card card--front" aria-label="Card front">
    <div class="mark-spot front-mark" role="img" aria-label="Organization mark"></div>
    <h1 class="wordmark-title front-title">Alder Ridge</h1>
    <p class="wordmark-tagline front-tagline">Helping Harbor</p>
    <p class="contact address">P.O. Box 287, Fernvale, Pa 18429</p>
    <dl class="contact phones">
      <dt>Phone</dt><dd>: (570) 413-CARE(2273)</dd><br>
      <dt>Toll Free</dt><dd>: (855) 413-CARE</dd>
    </dl>
    <dl class="contact emails">
      <dt>E-mail</dt><dd>:Info@alderridgehh.org</dd>
      <span class="line2">:Careline@alderridgehh.org</span>
    </dl>
    <p class="front-web">www.alderridgehh.org</p>
  </section>

  <section class="card card--back" aria-label="Card back">
    <blockquote class="verse">
      I was hungry and you gave me something to eat;<br>
      "I was thirsty and you gave me something to drink;<br>
      "I was a stranger and you invited me in."
    </blockquote>
    <p class="verse-ref">Matthew 25:35</p>
    <p class="wordmark-title back-title">Alder Ridge</p>
    <p class="wordmark-tagline back-tagline">Helping Harbor</p>
    <div class="mark-spot back-mark" role="img" aria-label="Organization mark"></div>
    <p class="back-web">www.alderridgehh.org</p>
  </section>
</main>
</body>
</html>
```